Food Safety 1-California workers only

3.25" by 4.5" Black and White Magazine Ad
This ad is to train California workers only.
Workers will be trained on: Food Safety, FSMA (Food Safety Modernization Act), using equipment safety, food processing production skills, worker safety, supervisory skills, communication skills.
"FREE TRAINING", The company does the training or Keystone Learning will provide the training.
Training grants range from $100,000 to $400,000.
Companies must be in business for profit.
Companies must train 200 employees or more.
This program is for California workers only.
Incumbent or new-hires are eligible.

Target Market(s)

California food processors, farms, food packaging, food processors, companies under FSMA, food safety, food production who need to train employees.

Industry/Entity Type

Food Production

Font styles to use
Serif
Sans Serif

Colors

Designer to choose colors to be used in the design.

Requirements
Must have
• This is a 3.25 inch by 4.5 inch magazine ad. It must be black and white. No color.
• The deliverable must be in basic PhotoShop. The ad does not need to include any graphics and be text only if needed. If you have a black and white graphic that will show well.
• Look at www.KLGFoodSafety..com
• Use the text from "MEALBOX-Photoshop-052018" file as your starting point.
Nice to have
• A black and white graphic about food. See www.KLGFoodSafety.com
Should not have
• No color.

```html
<!DOCTYPE html>
<html lang="en">
<head>
<meta charset="utf-8">
<title>Free Training Ad</title>
<link rel="stylesheet" href="https://fonts.googleapis.com/css2?family=Cinzel:wght@700;900&family=Playfair+Display:ital,wght@1,700&family=Roboto+Condensed:wght@400;700&display=swap">
<style>
  :root {
    --ink: #111111;
    --paper: #ffffff;
    --page: #e9e9e9;
    --photo-dark: #5a5a5a;
    --photo-mid: #9a9a9a;
    --photo-light: #d4d4d4;
    --rule: #222222;
  }
  * { box-sizing: border-box; margin: 0; padding: 0; }
  html, body { width: 1200px; height: 800px; overflow: hidden; background: var(--page); }
  body { display: flex; align-items: center; justify-content: center; }

  .ad {
    width: 520px; height: 720px;
    background: var(--paper);
    border: 3px solid var(--ink);
    padding: 10px;
    display: flex; flex-direction: column;
    font-family: "Roboto Condensed", Arial, sans-serif;
    color: var(--ink);
  }

  .hero {
    position: relative; height: 330px;
    border: 1px solid var(--ink);
    overflow: hidden;
  }
  .hero-photo {
    position: absolute; inset: 0;
    background: linear-gradient(135deg, var(--photo-light) 0%, var(--photo-mid) 45%, var(--photo-dark) 100%);
  }
  .hero-food {
    position: absolute; left: 38%; bottom: 34px;
    width: 96px; height: 96px; border-radius: 50%;
    background: radial-gradient(circle, #f2f2f2 0%, #bcbcbc 100%);
  }
  .hero-title {
    position: absolute; top: 46px; left: 0; right: 0;
    text-align: center;
    font-family: "Cinzel", "Times New Roman", serif; font-weight: 900;
    font-size: 58px; line-height: 0.95; letter-spacing: 2px;
    color: var(--paper);
    text-shadow: 2px 3px 0 var(--ink);
  }
  .hero-banner {
    position: absolute; top: 178px; left: 60px; right: 70px;
    background: var(--paper);
    padding: 6px 10px;
    text-align: center;
    font-family: "Playfair Display", Georgia, serif; font-style: italic; font-weight: 700;
    font-size: 17px; line-height: 1.15; text-transform: uppercase;
  }

  .topics {
    margin-top: 12px;
    padding: 6px 0;
    border-top: 2px solid var(--rule); border-bottom: 2px solid var(--rule);
    text-align: center; font-weight: 700; font-size: 19px; letter-spacing: 0.3px;
  }

  .qualify { margin-top: 18px; flex: 1; }
  .qualify-title {
    text-align: center; font-weight: 700; font-size: 24px; margin-bottom: 12px;
  }
  .qualify-list {
    display: grid; grid-template-columns: 1fr 1fr; gap: 10px 22px;
    list-style: none; padding: 0 10px;
  }
  .qualify-item {
    display: flex; gap: 7px; font-size: 16px; line-height: 1.2;
  }
  .check { flex: none; width: 15px; height: 15px; margin-top: 2px; }

  .contact {
    background: var(--ink); color: var(--paper);
    padding: 14px 10px; text-align: center;
    font-size: 14.5px; line-height: 1.6;
  }
</style>
</head>
<body>
  <article class="ad">
    <header class="hero">
      <div class="hero-photo" role="img" aria-label="Black and white photo of chefs working in a commercial kitchen"></div>
      <div class="hero-food" role="img" aria-label="Circular inset photo of food ingredients"></div>
      <h1 class="hero-title">FREE<br>TRAINING</h1>
      <p class="hero-banner">"We do the training and<br>the state pays for it!"</p>
    </header>

    <p class="topics">FOOD SAFETY • FSMA • PRODUCTION SKILLS • WORKER SAFETY</p>

    <section class="qualify">
      <h2 class="qualify-title">HOW TO QUALIFY:</h2>
      <ul class="qualify-list">
        <li class="qualify-item"><svg class="check" viewBox="0 0 16 16"><rect x="1" y="3" width="11" height="11" fill="none" stroke="#111" stroke-width="1.4"/><path d="M3.5 8.5l3 3 8-9" fill="none" stroke="#111" stroke-width="1.8"/></svg>Train California Workers Only</li>
        <li class="qualify-item"><svg class="check" viewBox="0 0 16 16"><rect x="1" y="3" width="11" height="11" fill="none" stroke="#111" stroke-width="1.4"/><path d="M3.5 8.5l3 3 8-9" fill="none" stroke="#111" stroke-width="1.8"/></svg>You must train 200 or more employees</li>
        <li class="qualify-item"><svg class="check" viewBox="0 0 16 16"><rect x="1" y="3" width="11" height="11" fill="none" stroke="#111" stroke-width="1.4"/><path d="M3.5 8.5l3 3 8-9" fill="none" stroke="#111" stroke-width="1.8"/></svg>Trainees must earn $11/hour</li>
        <li class="qualify-item"><svg class="check" viewBox="0 0 16 16"><rect x="1" y="3" width="11" height="11" fill="none" stroke="#111" stroke-width="1.4"/><path d="M3.5 8.5l3 3 8-9" fill="none" stroke="#111" stroke-width="1.8"/></svg>Incumbent or New-Hire workers are eligible</li>
        <li class="qualify-item"><svg class="check" viewBox="0 0 16 16"><rect x="1" y="3" width="11" height="11" fill="none" stroke="#111" stroke-width="1.4"/><path d="M3.5 8.5l3 3 8-9" fill="none" stroke="#111" stroke-width="1.8"/></svg>Full-time workers only</li>
        <li class="qualify-item"><svg class="check" viewBox="0 0 16 16"><rect x="1" y="3" width="11" height="11" fill="none" stroke="#111" stroke-width="1.4"/><path d="M3.5 8.5l3 3 8-9" fill="none" stroke="#111" stroke-width="1.8"/></svg>Seasonal workers are eligible</li>
        <li class="qualify-item"><svg class="check" viewBox="0 0 16 16"><rect x="1" y="3" width="11" height="11" fill="none" stroke="#111" stroke-width="1.4"/><path d="M3.5 8.5l3 3 8-9" fill="none" stroke="#111" stroke-width="1.8"/></svg>Employees must attend at least 8 Hours of training</li>
      </ul>
    </section>

    <footer class="contact">
      <p>Contact Daniel Morrow | Keystone Learning Company, Inc. | &#9742; (555) 014-2290</p>
      <p>1200 Harbor View Drive, Suite 310, Lakeview, CA 90000</p>
      <p>www.KLGCAL.com | www.KLGFoodSafety.com | &#9993; Dan.Morrow@KLGCAL.com</p>
    </footer>
  </article>
</body>
</html>
```